Clean Stylish Hip Online Marketplace Website Design

I am needing a seasoned designer with a hipster flair to design an online marketplace that connects people with others who can provide home and professional baking services in their local area. Need maps, feature driven and above all an identifiable LOOK to the site that is clean, trustworthy and inviting. (Online Marketplace service like Nestquill, Pawlix.com, ArtFlockly but with the look of Wandermaptour.com, Zipo, halloworchard.com)

Target Market(s)

Women, special occasion hosts, Moms, Bride-to-be

Industry/Entity Type

Marketplace

Number of Pages Required

5+ page

Font styles to use
Serif
Sans Serif

Requirements
Must have
• Modern, subtle feminine elements, hip. 2 options for user on home page similar to art flockly 1) Become a CrumbKeeper 2) Post or Search For Your Dessert. ABOUT, Categories (list of baked goods), Browse Projects, How it works, Log in. Profile set up page and profile of bakers with their uploaded photos of their baked items. Post for a project page where user can go it in request all bakers in the area for a baked good. Name, City Baked good,Date/Time needed, Description of Project and submit button. List of all the projects where bakers can accept or decline project with a bid. Payment Page.
Nice to have
• Map capabilities somewhere for people to filter down by location. Be able to showcase bakers cake or cookies photos in a beautiful unique and stylish way.
Should not have
• Nothing too girly or corporate. I am looking for a very stylized website for an online marketplace.

```html
<!DOCTYPE html>
<html lang="en">
<head>
<meta charset="utf-8">
<title>CrumbKeeper – Our Projects</title>
<link href="https://fonts.googleapis.com/css2?family=Montserrat:wght@400;500;600;700&display=swap" rel="stylesheet">
<style>
  :root{
    --pink:#e8156b;
    --orange:#f6893a;
    --ink:#1c1c1c;
    --text:#3a3a3a;
    --muted:#777;
    --line:#e6e6e6;
    --page:#f8f8f8;
    --white:#ffffff;
  }
  *{box-sizing:border-box;margin:0;padding:0}
  html,body{width:1200px;height:2826px;overflow:hidden}
  body{position:relative;background:var(--page);font-family:"Montserrat",Arial,sans-serif;color:var(--text)}

  .site-header{position:absolute;left:0;top:0;width:1200px;height:107px;background:var(--white);border-bottom:1px solid var(--line)}
  .brand{position:absolute;left:201px;top:38px;display:flex;align-items:center;white-space:nowrap}
  .brand-name{font-size:20px;font-weight:500;color:var(--ink);letter-spacing:0}
  .brand-divider{width:1px;height:30px;background:#999;margin:0 9px}
  .brand-tagline{font-size:8px;color:var(--ink)}
  .main-nav{position:absolute;top:42px;left:575px;display:flex;align-items:flex-start;white-space:nowrap}
  .main-nav a{font-size:11px;color:var(--ink);text-decoration:none;margin-right:22px;line-height:20px;padding-bottom:7px;border-bottom:2px solid transparent}
  .main-nav a.active{border-bottom-color:var(--orange)}
  .main-nav .login-btn{width:73px;height:22px;line-height:22px;padding:0;border:0;text-align:center;background:var(--orange);color:var(--white);border-radius:3px;font-size:10px;margin:0 0 0 4px}

  .intro{position:absolute;left:198px;top:130px}
  .intro h1{font-size:24px;font-weight:500;color:var(--pink);line-height:30px}
  .intro p{font-size:15px;color:var(--text);letter-spacing:.3px;margin-top:2px}
  .search-box{position:absolute;left:575px;top:132px;width:422px;height:56px;background:var(--white);border:1px solid var(--line);border-radius:4px;box-shadow:0 1px 3px rgba(0,0,0,.05)}
  .search-box span{position:absolute;left:16px;top:20px;font-size:10px;color:#aaa}
  .search-box svg{position:absolute;right:14px;top:20px}

  .section-title{position:absolute;left:0;width:1200px;top:273px;text-align:center;font-size:24px;font-weight:500;color:var(--ink)}

  .project-list{position:absolute;left:202px;top:339px;width:796px;display:flex;flex-direction:column;gap:66px}
  .project-card{position:relative;height:307px;display:flex;background:var(--white);box-shadow:0 2px 4px rgba(0,0,0,.08)}
  .project-info{position:relative;width:476px}
  .date-badge{position:absolute;left:26px;top:45px;width:75px;height:93px;background:var(--pink);color:var(--white);text-align:center;padding-top:8px}
  .date-day{font-size:36px;line-height:36px}
  .date-month{font-size:11px;line-height:14px;letter-spacing:.5px}
  .date-year{font-size:21px;line-height:24px}
  .project-body{position:absolute;left:116px;top:40px}
  .project-title{font-size:24px;font-weight:400;color:var(--orange);line-height:30px}
  .project-client{font-size:16px;color:var(--text);margin-bottom:18px}
  .project-meta{font-size:15px;line-height:27px;color:var(--text)}
  .project-meta b{font-weight:600;color:var(--ink)}
  .project-actions{display:flex;gap:8px;margin-top:22px}
  .btn{height:34px;line-height:34px;border-radius:6px;color:var(--white);font-size:14px;font-weight:600;text-align:center}
  .btn-pick{width:161px;background:var(--orange)}
  .btn-bid{width:102px;background:var(--pink)}
  .project-photo{width:320px;height:307px}

  .pagination{position:absolute;left:446px;top:2579px;display:flex;align-items:center;gap:9px}
  .page{width:20px;height:20px;border:1px solid #ccc;border-radius:2px;font-size:8px;line-height:18px;text-align:center;color:var(--ink);background:var(--white)}
  .page.current{background:var(--ink);color:var(--white);border-color:var(--ink)}
  .page-gap{width:20px;text-align:center;font-size:10px;color:var(--muted)}
  .see-more{position:absolute;left:473px;top:2649px;width:252px;height:51px;line-height:51px;background:var(--pink);color:var(--white);text-align:center;font-size:16px;border-radius:3px}

  .site-footer{position:absolute;left:0;top:2756px;width:1200px;height:70px;border-top:1px solid var(--line);text-align:center;font-size:11px;color:var(--ink);padding-top:30px}
</style>
</head>
<body>
  <header class="site-header">
    <div class="brand">
      <span class="brand-name">CRUMBKEEPER.COM</span>
      <span class="brand-divider"></span>
      <span class="brand-tagline">Bringing Local Bakers to You</span>
    </div>
    <nav class="main-nav">
      <a class="active" href="#">About Us</a>
      <a href="#">Categories</a>
      <a href="#">Browse Projects</a>
      <a href="#">How it Works</a>
      <a class="login-btn" href="#">LOGIN</a>
    </nav>
  </header>

  <div class="intro">
    <h1>PREVIEW LOCAL BAKERS</h1>
    <p>POST or SEARCH FOR A DESSERT</p>
  </div>
  <div class="search-box">
    <span>Search for Baker, Specialty, Location, etc</span>
    <svg width="14" height="14" viewBox="0 0 14 14"><circle cx="6" cy="6" r="4.2" fill="none" stroke="#e8156b" stroke-width="2"/><line x1="9" y1="9" x2="12.5" y2="12.5" stroke="#e8156b" stroke-width="2"/></svg>
  </div>

  <h2 class="section-title">OUR PROJECTS</h2>

  <main class="project-list">
    <article class="project-card">
      <div class="project-info">
        <div class="date-badge"><div class="date-day">22</div><div class="date-month">MARCH</div><div class="date-year">2017</div></div>
        <div class="project-body">
          <h3 class="project-title">Baker for Seven Spirals</h3>
          <p class="project-client">Seven Spirals</p>
          <p class="project-meta"><b>Job:</b> Baker<br><b>Location:</b> Edinburgh<br><b>Remuneration:</b> Dependent on experience</p>
          <div class="project-actions"><span class="btn btn-pick">PICK PROJECT</span><span class="btn btn-bid">BID NOW</span></div>
        </div>
      </div>
      <div class="project-photo" role="img" aria-label="Baker holding a tray of croissants in a bakery" style="background:linear-gradient(135deg,#c98a4a,#e9dccb 55%,#8a5a32)"></div>
    </article>

    <article class="project-card">
      <div class="project-info">
        <div class="date-badge"><div class="date-day">22</div><div class="date-month">MARCH</div><div class="date-year">2017</div></div>
        <div class="project-body">
          <h3 class="project-title">Baker for Seven Spirals</h3>
          <p class="project-client">Seven Spirals</p>
          <p class="project-meta"><b>Job:</b> Baker<br><b>Location:</b> Edinburgh<br><b>Remuneration:</b> Dependent on experience</p>
          <div class="project-actions"><span class="btn btn-pick">PICK PROJECT</span><span class="btn btn-bid">BID NOW</span></div>
        </div>
      </div>
      <div class="project-photo" role="img" aria-label="Baker in white jacket holding a tray of bread rolls" style="background:linear-gradient(160deg,#d8d2c8,#f1eee9 50%,#a9764a)"></div>
    </article>

    <article class="project-card">
      <div class="project-info">
        <div class="date-badge"><div class="date-day">22</div><div class="date-month">MARCH</div><div class="date-year">2017</div></div>
        <div class="project-body">
          <h3 class="project-title">Baker for Seven Spirals</h3>
          <p class="project-client">Seven Spirals</p>
          <p class="project-meta"><b>Job:</b> Baker<br><b>Location:</b> Edinburgh<br><b>Remuneration:</b> Dependent on experience</p>
          <div class="project-actions"><span class="btn btn-pick">PICK PROJECT</span><span class="btn btn-bid">BID NOW</span></div>
        </div>
      </div>
      <div class="project-photo" role="img" aria-label="Smiling baker in a chef hat with loaves of bread" style="background:linear-gradient(135deg,#e0962f,#f3e3cc 55%,#c47a2e)"></div>
    </article>

    <article class="project-card">
      <div class="project-info">
        <div class="date-badge"><div class="date-day">22</div><div class="date-month">MARCH</div><div class="date-year">2017</div></div>
        <div class="project-body">
          <h3 class="project-title">Baker for Seven Spirals</h3>
          <p class="project-client">Seven Spirals</p>
          <p class="project-meta"><b>Job:</b> Baker<br><b>Location:</b> Edinburgh<br><b>Remuneration:</b> Dependent on experience</p>
          <div class="project-actions"><span class="btn btn-pick">PICK PROJECT</span><span class="btn btn-bid">BID NOW</span></div>
        </div>
      </div>
      <div class="project-photo" role="img" aria-label="Baker in an apron holding a tray of pastries in a shop" style="background:linear-gradient(160deg,#8a5b34,#caa47c 50%,#5e3d22)"></div>
    </article>

    <article class="project-card">
      <div class="project-info">
        <div class="date-badge"><div class="date-day">22</div><div class="date-month">MARCH</div><div class="date-year">2017</div></div>
        <div class="project-body">
          <h3 class="project-title">Baker for Seven Spirals</h3>
          <p class="project-client">Seven Spirals</p>
          <p class="project-meta"><b>Job:</b> Baker<br><b>Location:</b> Edinburgh<br><b>Remuneration:</b> Dependent on experience</p>
          <div class="project-actions"><span class="btn btn-pick">PICK PROJECT</span><span class="btn btn-bid">BID NOW</span></div>
        </div>
      </div>
      <div class="project-photo" role="img" aria-label="Baker taking a tray of buns from the oven" style="background:linear-gradient(160deg,#6f8a8e,#c9c4b8 50%,#9a6a3c)"></div>
    </article>

    <article class="project-card">
      <div class="project-info">
        <div class="date-badge"><div class="date-day">22</div><div class="date-month">MARCH</div><div class="date-year">2017</div></div>
        <div class="project-body">
          <h3 class="project-title">Baker for Seven Spirals</h3>
          <p class="project-client">Seven Spirals</p>
          <p class="project-meta"><b>Job:</b> Baker<br><b>Location:</b> Edinburgh<br><b>Remuneration:</b> Dependent on experience</p>
          <div class="project-actions"><span class="btn btn-pick">PICK PROJECT</span><span class="btn btn-bid">BID NOW</span></div>
        </div>
      </div>
      <div class="project-photo" role="img" aria-label="Chef in a white hat cutting a pizza" style="background:linear-gradient(160deg,#3d3d3f,#9a9896 50%,#7a4a2c)"></div>
    </article>
  </main>

  <nav class="pagination" aria-label="Pages">
    <span class="page">
      <svg width="8" height="8" viewBox="0 0 8 8"><path d="M5 1 2 4l3 3" fill="none" stroke="#1c1c1c" stroke-width="1.2"/></svg>
    </span>
    <span class="page">1</span>
    <span class="page">2</span>
    <span class="page">3</span>
    <span class="page current">4</span>
    <span class="page">5</span>
    <span class="page-gap">…</span>
    <span class="page">15</span>
    <span class="page">30</span>
    <span class="page">45</span>
    <span class="page">
      <svg width="8" height="8" viewBox="0 0 8 8"><path d="M3 1l3 3-3 3" fill="none" stroke="#1c1c1c" stroke-width="1.2"/></svg>
    </span>
  </nav>

  <div class="see-more">SEE MORE PROJECTS</div>

  <footer class="site-footer">© 2016 &nbsp;Company Name &nbsp;| All Rights Reserved</footer>
</body>
</html>
```